Newsletter March April 2020

create a newsletter to send to client which is informative and visually impactful

previous projects attached

Target Market(s)

property market

Industry/Entity Type

Property

Colors
abd037

Requirements
Must have
• company logo
www.veltrampage.co.uk
Nice to have
• colour inline with logo etc
graphics to show data where possible

```html
<!DOCTYPE html>
<html lang="en">
<head>
<meta charset="utf-8">
<title>Newsletter March April 2020</title>
<link rel="stylesheet" href="https://fonts.googleapis.com/css2?family=Arimo:wght@400;700&family=Noto+Sans:wght@700;800&display=swap">
<style>
  :root {
    --page-green: #33cc33;
    --deep-green: #063806;
    --box-green: #006622;
    --glow: #a8ee9e;
    --ink-light: #ffffff;
    --ink-box: #1a1a1a;
    --canvas: #ffffff;
  }
  * { margin: 0; padding: 0; box-sizing: border-box; }
  html, body { width: 1200px; height: 776px; overflow: hidden; background: var(--canvas); }
  .spread { position: relative; width: 1200px; height: 776px; }
  .page {
    position: absolute; top: 34px; width: 548px; height: 707px;
    background: var(--page-green);
    box-shadow: 0 0 8px 2px var(--glow);
    font-family: "Arimo", Arial, sans-serif;
    color: var(--ink-light);
  }
  .page--left { left: 32px; }
  .page--right { left: 620px; }
  .page-corner { position: absolute; top: 0; right: 0; width: 80px; height: 80px; }
  .page-number {
    position: absolute; top: 16px; right: 14px;
    font-family: "Noto Sans", Verdana, sans-serif; font-weight: 800; font-size: 20px; color: var(--ink-light);
  }
  .page-title {
    position: absolute; left: 26px;
    font-family: "Noto Sans", Verdana, sans-serif; font-weight: 800;
    color: var(--deep-green); font-size: 23px; line-height: 24px; letter-spacing: 0.3px;
  }
  .page-title--feature { top: 37px; width: 480px; text-align: justify; text-align-last: left; }
  .page-title--feature .spread-line { display: block; text-align: justify; text-align-last: justify; }
  .page-title--plain { top: 36px; }
  .body-copy { position: absolute; font-size: 11.4px; line-height: 12.8px; text-align: justify; }
  .section-heading {
    position: absolute; left: 26px;
    font-family: "Noto Sans", Verdana, sans-serif; font-weight: 700;
    font-size: 13.6px; line-height: 18px; color: var(--deep-green);
  }
  .accent-bar { position: absolute; background: var(--deep-green); }
  .info-box { position: absolute; left: 304px; top: 208px; width: 222px; height: 465px; background: #fff; border: 1px solid var(--deep-green); }
  .info-box__head {
    height: 47px; background: var(--box-green); color: var(--ink-light);
    font-family: "Noto Sans", Verdana, sans-serif; font-weight: 700; font-size: 13.6px;
    display: flex; align-items: center; justify-content: center;
  }
  .info-box__text { padding: 27px 16px 0 16px; color: var(--ink-box); font-size: 11.4px; line-height: 12.8px; text-align: justify; }
  .frame-art { position: absolute; left: 0; top: 0; }
  .banner-question {
    position: absolute; left: 50px; top: 101px;
    font-family: "Noto Sans", Verdana, sans-serif; font-weight: 700; font-size: 13.6px; color: var(--ink-light);
  }
</style>
</head>
<body>
<div class="spread">

  <section class="page page--left">
    <svg class="page-corner" viewBox="0 0 80 80" aria-hidden="true"><polygon points="0,0 80,0 80,80" fill="var(--deep-green)"/></svg>
    <span class="page-number">2</span>

    <h1 class="page-title page-title--feature">
      <span class="spread-line">Domestic EPC - Minimum energy</span>
      <span class="spread-line">efficiency standards rollout to</span>
      existing tenancies from April 2020
    </h1>

    <div class="accent-bar" style="left:26px;top:124px;width:18px;height:182px"></div>
    <p class="body-copy" style="left:62px;top:138px;width:448px">Since April 2018, new tenancies in England and Wales have had to meet the Government’s minimum energy efficiency standard (MEES). Properties which require an energy performance certificate (EPC) must reach a minimum ‘E’ rating on their EPC assessment, or have a valid exemption registered.</p>
    <p class="body-copy" style="left:62px;top:204px;width:226px">Last year, the Government introduced a ‘cost cap’, requiring landlords to spend up to £3,500 per property to improve them to the minimum level.<br>From 1 April 2020, this requirement is extending to all existing tenancies. Here’s what you need to know.</p>

    <h2 class="section-heading" style="top:311px;width:262px">Who needs to upgrade their properties?</h2>
    <p class="body-copy" style="left:26px;top:356px;width:262px">The Government is introducing a minimum band E rating for properties let in England and Wales. This currently applies to all new lets – at the change of tenancy or on renewal – but from April this year will also apply to all existing tenancies, where a valid EPC exists. Landlords must pay up to £3,500 per property to improve any properties currently rated F or G, known as the ‘MEES cost cap’</p>

    <h2 class="section-heading" style="top:482px;width:270px">What if the cost of improving to an ‘E’ is higher than £3,500?</h2>
    <p class="body-copy" style="left:26px;top:527px;width:262px">If the cost of reaching an E rating is higher than £3,500, you will need to register an exemption – either a ‘high cost exemption’ if the cost of installing the cheapest recommended improvement is higher, or the ‘all improvements made exemption’ if improvements up to the value of £3,500 have been made but the property remains rated F or G.<br>The PRS Exemptions Register is held by the Government. Landlords must upload evidence of the exemption cited when they register. Each exemption is valid for a maximum of five years.</p>

    <aside class="info-box">
      <div class="info-box__head">What is an EPC?</div>
      <p class="info-box__text">EPCs are certificates which indicate how energy efficient a property is currently, and could be with improvements. The rating for the EPC is based on an assessment undertaken by an accredited domestic energy assessor. It is based on the ‘fabric’ of the building i.e. how it is constructed and materials, and the ‘services’ e.g. heating, ventilation and lighting. Points are given for each of the energy efficient measures in place – which results in a ‘SAP’ (standard assessment procedure) rating. This is then converted into an ‘EPC band’ or rating – ranging from A for the most efficient to G for the most inefficient.<br>EPCs are a legal requirement for buildings when constructed, let, or sold. Individual rooms let within an HMO do not require separate EPCs, but if the HMO has been let on a single tenancy or sold in the last 10 years, the building will require one.</p>
    </aside>
  </section>

  <section class="page page--right">
    <svg class="frame-art" width="548" height="707" viewBox="0 0 548 707" aria-hidden="true">
      <polygon points="26,82 458,82 516,138 44,138 44,326 26,326" fill="var(--deep-green)"/>
      <rect x="26" y="358" width="18" height="57" fill="var(--deep-green)"/>
      <rect x="26" y="452" width="18" height="46" fill="var(--deep-green)"/>
      <polygon points="26,554 44,554 44,650 516,650 502,670 26,670" fill="var(--deep-green)"/>
    </svg>
    <svg class="page-corner" viewBox="0 0 80 80" aria-hidden="true"><polygon points="0,0 80,0 80,80" fill="var(--deep-green)"/></svg>
    <span class="page-number">3</span>

    <h1 class="page-title page-title--plain">Upcoming changes</h1>
    <p class="banner-question">Are there any more regulations on the horizon?</p>

    <p class="body-copy" style="left:70px;top:151px;width:445px">The UK Government has committed to net-zero carbon emissions by 2050. Improving the carbon footprint of housing will be a key objective for them over the coming years, and we expect properties in the private rented sector to be required to meet a minimum C rating by 2030, and an A rating before 2050.<br>In addition, the Government will be banning gas boilers from new build properties by 2025 – and in time will likely phase gas out from existing properties. Carbon dioxide emissions from the residential sector are currently around 18 percent of the UK total, according to Government statistics, with gas for heating and cooking one of the main sources – so will be a key target.<br>As these changes come in, new and unfamiliar technologies, such as air source and ground source heat pumps, will become more common, and prices of these will fall. But we’d advise landlords to consider where they can make improvements to their properties as part of their business cycle to get ahead of the game – for example, during void periods.</p>

    <h2 class="section-heading" style="top:341px">What about commercial properties?</h2>
    <p class="body-copy" style="left:70px;top:366px;width:452px">Since April 2018 all new tenancies in England and Wales have had to achieve MEES, just like domestic properties. However the requirement extending to all leases does not start until April 2023. A consultation period has recently ended into setting new targets of minimum Band B/C by 2030 for commercial buildings.</p>

    <h2 class="section-heading" style="top:432px">Does MEES apply to property sales?</h2>
    <p class="body-copy" style="left:70px;top:460px;width:445px">MEES only applies to the rental sector. Properties for sale will still need an EPC but not of a minimum band E. However potential buyers may be put off by a low energy rating if they plan to buy and let the property.</p>

    <h2 class="section-heading" style="top:514px;width:500px">My building EPC is band G, does this mean significant amounts of money will need to be spent to bring up to standard?</h2>
    <p class="body-copy" style="left:70px;top:560px;width:445px">At Veltram Page we have reassessed many previously rated band F and G properties and have found them to recalculate at a much improved rating, this requiring no works to be needed. Previous assessments may have used default ratings or missed key details which had a negative impact on the asset rating.</p>
    <p class="body-copy" style="left:70px;top:617px;width:445px">If a new assessment of your property does result in the rating being band F or G we can assist in informing you of cost effective ways to improve the rating.</p>
  </section>

</div>
</body>
</html>
```